Logo & Web Design for Technical Research Products

Logo and Web Design for a little business selling some niche research, technical products. Current site is at: http://mavrite-lab.com/mavrite-lab-ionic-bench-unit. The audience are university researchers, technical labs and similar.

We would like a more professional looking logo and design than what is currently there.

This new design should include/consider:
- A front page with the ability to show-case 2-3 select products
- An About Us page
- A Contact Us page
- An FAQ page
- A hierarchical menu structure (preferably to the left) allowing for at least two levels. (We plan to add more products and categories in the future)
- Include both a Desktop and Phone version (responsive design)
- We plan to have all products follow a similar template so please have that in mind when desiging (Some part of the product template may be omitted for some products if not applicable)
- Multiple images per product should be supported(carousel perhaps?)

When creating the CSS and HTML please use Bootstap 4.
(https://framelyt.dev/docs/4.0/getting-started/introduction/)

```html
<!DOCTYPE html>
<html lang="en">
<head>
<meta charset="utf-8">
<title>MavriteLab – Research Products</title>
<link rel="stylesheet" href="https://fonts.googleapis.com/css2?family=Poppins:wght@300;400;500;600;700&display=swap">
<style>
:root{
  --blue:#2196e3;
  --blue-dark:#1578c4;
  --navy:#0d1a30;
  --navy-2:#16284a;
  --ink:#1b1b1b;
  --muted:#7a8391;
  --line:#e3e7ec;
  --white:#ffffff;
  --card-shadow:0 8px 24px rgba(20,40,80,.12);
}
*{box-sizing:border-box;margin:0;padding:0}
html,body{width:1200px;height:2968px;overflow:hidden}
body{position:relative;background:var(--white);font-family:'Poppins',sans-serif;color:var(--ink)}

/* Header + hero */
.hero-bg{position:absolute;left:0;top:0}
.brand{position:absolute;left:36px;top:24px;font-size:30px;font-weight:700;color:var(--white);letter-spacing:.5px}
.nav{position:absolute;right:52px;top:42px;display:flex;align-items:center;gap:34px;list-style:none}
.nav a{color:var(--white);text-decoration:none;font-size:13px;font-weight:500;letter-spacing:.5px}
.nav .nav-cta{background:rgba(255,255,255,.22);padding:12px 16px}
.hero-text{position:absolute;left:140px;top:168px;color:var(--white);width:380px}
.hero-text .pre{font-size:38px;font-weight:400;line-height:1.1}
.hero-text h1{font-size:74px;font-weight:700;line-height:1.05}
.hero-text p{font-size:14px;line-height:1.5;margin-top:10px;opacity:.95}
.btn-light{display:inline-block;margin-top:30px;background:var(--white);color:var(--ink);font-size:12px;font-weight:600;padding:13px 22px;letter-spacing:.5px}
.hero-photo{position:absolute;left:720px;top:90px}

/* Biography */
.bio-kicker{position:absolute;left:140px;top:686px;color:var(--blue);font-size:36px;font-weight:700;letter-spacing:1px}
.bio-title{position:absolute;left:140px;top:722px;font-size:66px;font-weight:700;color:var(--ink)}
.bio-rule{position:absolute;left:88px;top:858px;width:70px;height:3px;background:var(--ink)}
.bio-col{position:absolute;top:840px;width:300px;font-size:13px;line-height:1.55;color:var(--muted)}
.bio-col p+p{margin-top:16px}
.btn-blue{position:absolute;background:var(--blue);color:var(--white);font-size:12px;font-weight:600;padding:16px 22px;letter-spacing:.5px}
.section-rule{position:absolute;left:88px;top:1062px;width:1024px;height:1px;background:var(--line)}

/* Products */
.section-title{position:absolute;left:0;width:1200px;text-align:center;font-size:40px;font-weight:600;color:var(--ink)}
.tabs{position:absolute;left:0;top:1174px;width:1200px;display:flex;justify-content:center;gap:32px;font-size:11px;font-weight:500;color:var(--ink)}
.tabs .active{color:var(--blue);border-bottom:2px solid var(--blue);padding-bottom:4px}
.card{position:absolute;top:1228px;width:325px;height:400px;background:var(--white);box-shadow:var(--card-shadow);padding:0 22px}
.card .shot{display:block;margin:20px auto 0;width:240px;height:190px;border-radius:4px}
.card h3{font-size:17px;font-weight:600;margin-top:20px}
.card p{font-size:12px;color:var(--muted);line-height:1.45;margin-top:6px}
.card .foot{position:absolute;left:22px;right:22px;bottom:28px;display:flex;justify-content:space-between;align-items:center}
.card .more{background:var(--blue);color:var(--white);font-size:10px;font-weight:600;padding:11px 16px}
.card .price{font-size:12px;color:var(--ink)}
.card .price b{color:var(--muted);font-weight:500;margin-left:8px}
.dots{position:absolute;left:582px;top:1664px;display:flex;gap:9px}
.dots span{width:10px;height:10px;border-radius:50%;background:#cfd6de}
.dots span:first-child{background:var(--blue)}

/* FAQ */
.faq-list{position:absolute;left:88px;top:1880px;width:504px;list-style:none}
.faq-list li{background:#f4f6f8;margin-bottom:18px;padding:14px 18px;font-size:12px;color:var(--ink)}
.faq-list li::before{content:"+";color:var(--blue);font-weight:600;margin-right:10px}
.faq-list li.open::before{content:"–"}
.faq-list li.open{background:var(--white);box-shadow:var(--card-shadow)}
.faq-list li.open p{margin:8px 0 0 20px;font-size:12px;color:var(--muted);line-height:1.5}
.faq-art{position:absolute;left:680px;top:1820px;width:440px;height:520px;border-radius:8px;background:linear-gradient(160deg,#f2f2f2,#d9dcdf 60%,#2a2a2a)}

/* Footer */
.footer-bg{position:absolute;left:0;top:2330px}
.news-title{position:absolute;left:0;top:2504px;width:1200px;text-align:center;color:var(--white);font-size:28px;font-weight:600}
.news-input{position:absolute;left:366px;top:2570px;width:468px;height:50px;background:var(--white);border-radius:25px;display:flex;align-items:center;padding:0 8px 0 20px;font-size:13px;color:#9aa3ad;gap:10px}
.news-input .go{margin-left:auto;width:36px;height:36px;border-radius:50%;background:var(--blue)}
.foot-brand{position:absolute;left:88px;top:2740px;font-size:34px;font-weight:700;color:var(--white);letter-spacing:.5px}
.foot-col{position:absolute;top:2690px;color:var(--white)}
.foot-col h4{font-size:15px;font-weight:500;color:#9aa6b8;margin-bottom:10px}
.foot-col a{display:block;color:var(--white);font-size:13px;line-height:1.75;text-decoration:none}
.social{display:flex;gap:10px}
.social span{width:30px;height:30px;border-radius:50%;background:var(--blue)}
.copyright{position:absolute;left:0;top:2926px;width:1200px;text-align:center;font-size:12px;color:#9aa6b8}
.to-top{position:absolute;left:1140px;top:2916px;width:40px;height:40px;border-radius:50%;background:var(--blue)}
</style>
</head>
<body>

<svg class="hero-bg" width="1200" height="600" viewBox="0 0 1200 600" aria-hidden="true">
  <defs>
    <linearGradient id="heroGrad" x1="0" y1="0" x2="1" y2="1">
      <stop offset="0" stop-color="#2aa2ee"/>
      <stop offset="1" stop-color="#1a86d6"/>
    </linearGradient>
  </defs>
  <path d="M0 0H1200V95C1010 110 860 190 760 320C640 470 330 560 0 520Z" fill="url(#heroGrad)"/>
</svg>

<header>
  <div class="brand">MAVRITELAB</div>
  <ul class="nav">
    <li><a href="#">HOME</a></li>
    <li><a href="#">ABOUT US</a></li>
    <li><a href="#">PRODUCTS</a></li>
    <li><a href="#">FAQ</a></li>
    <li><a class="nav-cta" href="#">CONTACT US</a></li>
  </ul>
</header>

<section class="hero-text">
  <div class="pre">Welcome to</div>
  <h1>MavriteLab</h1>
  <p>If you have any questions or wish to purchase any of our products we can be contacted at anytime.</p>
  <span class="btn-light">GET STARTED</span>
</section>

<svg class="hero-photo" width="480" height="480" viewBox="0 0 480 480" role="img" aria-label="Photo of a researcher assembling a lab device">
  <defs>
    <linearGradient id="photoGrad" x1="0" y1="0" x2="1" y2="1">
      <stop offset="0" stop-color="#e9e7e3"/>
      <stop offset=".55" stop-color="#b79a82"/>
      <stop offset="1" stop-color="#7d2d2b"/>
    </linearGradient>
  </defs>
  <circle cx="240" cy="240" r="236" fill="url(#photoGrad)" stroke="#ffffff" stroke-width="6"/>
</svg>

<section class="bio">
  <div class="bio-kicker">SHORT</div>
  <h2 class="bio-title">Biography</h2>
  <div class="bio-rule"></div>
  <div class="bio-col" style="left:190px">
    <p>Aenean imperdiet etiam ultricies nisi vel augue curabitur ullamcorper ultricies nisi nam eget dui etiam rhoncus tellus eget condimentum rhoncus sem quam.</p>
    <p>Nullam nisi vel augue curabitur ullamcorper ultricies nisi nam eget dui etiam rhoncus maecenas tempus.</p>
  </div>
  <div class="bio-col" style="left:598px">
    <p>Ultricies nisi vel augue curabitur ullamcorper ultricies nisi nam eget dui etiam rhoncus.</p>
    <p>Imperdiet etiam ultricies nisi vel augue curabitur ullamcorper ultricies nisi nam eget dui etiam rhoncus maecenas tempus tellus eget condimentum rhoncus sem quam.</p>
  </div>
  <span class="btn-blue" style="left:1056px;top:912px">LEARN MORE</span>
  <div class="section-rule"></div>
</section>

<section class="products">
  <h2 class="section-title" style="top:1102px">Our Products</h2>
  <div class="tabs">
    <span class="active">ALL</span>
    <span>BATTERY TESTER</span>
    <span>IONIC BENCH TEST CELL</span>
    <span>PHOTOELECTROCHEMICAL TEST CELL</span>
    <span>2 CHANNEL PERISTALTIC PUMP</span>
  </div>

  <article class="card" style="left:88px">
    <div class="shot" role="img" aria-label="Product photo of an 8 channel battery tester" style="background:linear-gradient(180deg,#eef1ee,#9fb3a6)"></div>
    <h3>8 channel battery tester</h3>
    <p>8 Channel battery tester with 5V range with either 0.5 (10%) 10mA or 10 mA.</p>
    <div class="foot"><span class="more">VIEW DETAILS</span><span class="price">Price <b>$ 2,700/-</b></span></div>
  </article>

  <article class="card" style="left:438px">
    <div class="shot" role="img" aria-label="Product photo of a flow battery test cell" style="background:linear-gradient(180deg,#e7ecf4,#4c68a8)"></div>
    <h3>Ionic Bench Test Cell</h3>
    <p>Ionic bench test cell (IBTC) test cell for tests of conventional flow batteries or others.</p>
    <div class="foot"><span class="more">VIEW DETAILS</span><span class="price">Price <b>$ 1,800/-</b></span></div>
  </article>

  <article class="card" style="left:788px">
    <div class="shot" role="img" aria-label="Product photo of a 2 channel peristaltic pump" style="background:linear-gradient(180deg,#f0f0f0,#8f9499)"></div>
    <h3>2 channel peristaltic pump</h3>
    <p>2 Channel peristaltic pump, ideal for circulating both solutions in either side.</p>
    <div class="foot"><span class="more">VIEW DETAILS</span><span class="price">Price <b>$ 2,000/-</b></span></div>
  </article>

  <div class="dots"><span></span><span></span><span></span></div>
</section>

<section class="faq">
  <h2 class="section-title" style="top:1744px">Frequently Asked Questions</h2>
  <ul class="faq-list">
    <li>Mauris mollis accumsan ipsum velit ?</li>
    <li>Aenean sollicitudin lorem quis bibendum auctor ?</li>
    <li>Elit consequat ipsum, nec sagittis sem nibh id elit ?</li>
    <li>Amet mauris, morbi accumsan ipsum velit ?</li>
    <li class="open">Sed non mauris vitae erat cursus ?
      <p>Aenean imperdiet etiam ultricies nisi vel augue curabitur ullamcorper ultricies nisi nam eget dui etiam rhoncus tellus eget condimentum rhoncus sem quam.</p>
    </li>
  </ul>
  <div class="faq-art" role="img" aria-label="Illustration of a thoughtful man beside large FAQ letters and a question mark"></div>
</section>

<svg class="footer-bg" width="1200" height="638" viewBox="0 0 1200 638" aria-hidden="true">
  <defs>
    <linearGradient id="footGrad" x1="0" y1="0" x2="0" y2="1">
      <stop offset="0" stop-color="#16284a"/>
      <stop offset=".35" stop-color="#0d1a30"/>
    </linearGradient>
  </defs>
  <path d="M0 10C240 120 420 110 640 70C880 30 1060 40 1200 120V638H0Z" fill="url(#footGrad)"/>
</svg>

<footer>
  <h2 class="news-title">Email Newsletter</h2>
  <div class="news-input">
    <svg width="16" height="12" viewBox="0 0 16 12" aria-hidden="true"><rect x=".5" y=".5" width="15" height="11" rx="1" fill="none" stroke="#9aa3ad"/><path d="M1 1l7 6 7-6" fill="none" stroke="#9aa3ad"/></svg>
    <span>Enter your email address</span>
    <span class="go"></span>
  </div>

  <div class="foot-brand">MAVRITELAB</div>

  <div class="foot-col" style="left:455px">
    <h4>Quick Links</h4>
    <a href="#">Home</a><a href="#">About Us</a><a href="#">Products</a><a href="#">Faq</a><a href="#">Contact Us</a>
  </div>
  <div class="foot-col" style="left:720px">
    <h4>Information</h4>
    <a href="#">Disclaimers</a><a href="#">Terms &amp; Conditions</a><a href="#">Privacy Policy</a>
  </div>
  <div class="foot-col" style="left:975px">
    <h4>Follow us</h4>
    <div class="social"><span></span><span></span><span></span></div>
  </div>

  <div class="copyright">© 2019. All Rights Reserved.</div>
  <div class="to-top">
    <svg width="40" height="40" viewBox="0 0 40 40" aria-hidden="true"><path d="M14 23l6-6 6 6" fill="none" stroke="#fff" stroke-width="2"/></svg>
  </div>
</footer>

</body>
</html>
```